Business Card Design Project

I want a design for my business cards based on an excisting logo design.

Target Market(s)

Marketeers, PR-peeps, CEO's, decisionmakers, entrepreneurs

Industry/Entity Type

Business

Requirements
Nice to have
• Some visual interest on the back too
Should not have
• Sarif on the font

```html
<!DOCTYPE html>
<html lang="nl">
<head>
<meta charset="utf-8">
<title>SproutPR – visitekaartje</title>
<link href="https://fonts.googleapis.com/css2?family=Open+Sans:wght@400;700&display=swap" rel="stylesheet">
<style>
  :root {
    --backdrop: #555457;
    --lime: #b3cb00;
    --lime-deep: #97b000;
    --lime-text: #a3c000;
    --paper: #ffffff;
    --paper-shade: #ececec;
    --ink-grey: #7a7a7a;
  }
  html, body {
    margin: 0;
    padding: 0;
    width: 1200px;
    height: 922px;
    overflow: hidden;
    background: var(--backdrop);
    font-family: "Open Sans", Verdana, sans-serif;
  }
  .canvas {
    position: relative;
    width: 1200px;
    height: 922px;
  }
  .card {
    position: absolute;
    top: 26px;
    width: 470px;
    height: 816px;
    border-radius: 17px;
    overflow: hidden;
    background: linear-gradient(100deg, var(--paper) 20%, var(--paper-shade) 100%);
  }
  .card--front { left: 111px; }
  .card--back { left: 631px; }

  /* Front */
  .front-visual {
    position: absolute;
    left: 0; top: 0;
    width: 100%;
    height: 595px;
    background:
      linear-gradient(120deg, rgba(255,255,255,0) 55%, rgba(255,255,255,0.12) 55%),
      radial-gradient(circle at 40% 35%, #bfd400 0%, var(--lime) 45%, var(--lime-deep) 100%);
  }
  .front-brand {
    position: absolute;
    left: 0;
    top: 650px;
    width: 100%;
    text-align: center;
  }
  .brand-dot {
    display: block;
    margin: 0 auto 18px;
    width: 100px;
    height: 100px;
    border-radius: 50%;
    background: var(--lime);
  }
  .front-brand .brand-name {
    font-size: 26px;
    color: var(--ink-grey);
    letter-spacing: 1px;
  }

  /* Back */
  .band {
    position: absolute;
    left: 0;
    width: 100%;
    background: var(--lime);
  }
  .band--top { top: 0; height: 54px; }
  .band--bottom { bottom: 0; height: 54px; }
  .back-brand {
    position: absolute;
    top: 152px;
    left: 30px;
    display: flex;
    align-items: center;
    gap: 16px;
  }
  .back-brand .brand-dot {
    margin: 0;
    width: 66px;
    height: 66px;
  }
  .back-brand .brand-name {
    font-size: 38px;
    color: var(--ink-grey);
    letter-spacing: 1px;
  }
  .contact {
    position: absolute;
    left: 0;
    width: 100%;
    text-align: center;
    color: var(--ink-grey);
    font-size: 24px;
    line-height: 31px;
    margin: 0;
  }
  .contact-name {
    top: 292px;
    color: var(--lime-text);
    font-weight: 700;
    font-size: 31px;
    line-height: 40px;
  }
  .contact-role { top: 340px; }
  .contact-phone { top: 497px; }
  .contact-address { top: 558px; }
  .contact-links {
    top: 650px;
    color: var(--lime-text);
    line-height: 32px;
  }
</style>
</head>
<body>
<main class="canvas">
  <section class="card card--front" aria-label="Voorzijde">
    <div class="front-visual" role="img" aria-label="Grote groene merkillustratie in limoentinten"></div>
    <div class="front-brand">
      <span class="brand-dot"></span>
      <span class="brand-name">SproutPR</span>
    </div>
  </section>

  <section class="card card--back" aria-label="Achterzijde">
    <div class="band band--top"></div>
    <div class="back-brand">
      <span class="brand-dot"></span>
      <span class="brand-name">SproutPR</span>
    </div>
    <p class="contact contact-name">Marit Jansen</p>
    <p class="contact contact-role">Systemisch en strategisch PR-,<br>marketing-<br>en communicatieadvies</p>
    <p class="contact contact-phone">+31(0)6 48203915</p>
    <p class="contact contact-address">Lindelaan 42<br>6711 AB Ede</p>
    <p class="contact contact-links">sproutpr.nl<br>twitter.com/_sproutpr<br>facebook.com/sproutpr</p>
    <div class="band band--bottom"></div>
  </section>
</main>
</body>
</html>
```